Lantern Gathering event flyer

I would like a church event flyer designed. The event is called "LANTERN GATHERING 2018". I am looking for a professional, yet catchy design that uses our brand colors and logo creatively while communicating key information of the event effectively.

1. The logo is attached in two color formats. The designer has the choice to use them as he/she want.

2. The location of the event is: Halvorn Community Center, 482 Tillman Street, Portland, ME 04107
3. Time and date of event. The designer can organize and format the date and time as he/she pleases.
December 28th, 29th @ 7:00PM
December 30th @ 10:00AM
4. The topic of the event is "Winds of morning". The designer is free to use this phrase as he/she pleases to create a good composition.
5. Speaker: Prophet Marcus Obuya
6. Contact information: contact@cedarbrookhaven.org - Telephone number: 207 555 3184

7. I would also like the following three words on the flyer. These words describe the focus of the event: FIRE, REVIVAL, PROPHETIC

```html
<!DOCTYPE html>
<html lang="en">
<head>
<meta charset="utf-8">
<title>Lantern Gathering 2018 Flyer</title>
<link href="https://fonts.googleapis.com/css2?family=Cinzel:wght@500&family=Montserrat:wght@800&family=Oswald:wght@600&family=Open+Sans&family=Encode+Sans+Condensed:wght@400&display=swap" rel="stylesheet">
<style>
  :root{
    --navy:#12365a;
    --navy-deep:#0b1a2b;
    --orange:#f2921f;
    --orange-light:#f7a63a;
    --white:#ffffff;
    --ink:#141414;
    --flame-a:#f6c341;
    --flame-b:#e9701c;
  }
  *{margin:0;padding:0;box-sizing:border-box}
  html,body{width:1200px;height:958px;overflow:hidden;background:var(--navy-deep)}
  .flyer{position:absolute;left:306px;top:41px;width:588px;height:876px;background:var(--white);overflow:hidden}
  .brand{position:absolute;top:60px;left:0;width:100%;text-align:center;font-family:"Cinzel",serif;font-weight:500;font-size:58px;color:var(--navy);letter-spacing:1px;display:flex;justify-content:center;align-items:center;gap:12px}
  .brand-dot{width:16px;height:16px;border-radius:50%;background:var(--orange)}
  .event-title{position:absolute;top:170px;left:0;width:100%;text-align:center;font-family:"Montserrat",sans-serif;font-weight:800;font-size:29px;color:var(--navy);letter-spacing:.5px}
  .theme-band{position:absolute;top:232px;left:0;width:100%;height:78px;background:linear-gradient(90deg,var(--flame-b),var(--flame-a) 30%,#f8d25c 50%,var(--flame-a) 70%,var(--flame-b))}
  .theme{position:absolute;top:236px;left:0;width:100%;text-align:center;font-family:"Oswald",sans-serif;font-weight:600;font-size:44px;color:#f4f0dc;text-shadow:0 0 3px #5b5a22,1px 1px 2px #3c3a14}
  .venue{position:absolute;top:336px;left:0;width:100%;height:136px;background:linear-gradient(90deg,var(--orange) 70%,#f7c98c 100%);text-align:center;font-family:"Open Sans",sans-serif;font-size:25px;line-height:37px;padding-top:12px;color:var(--white)}
  .venue-label{color:var(--navy)}
  .speaker-tag{position:absolute;top:476px;left:0;width:334px;height:62px;background:var(--white);box-shadow:6px 0 10px rgba(0,0,0,.06);font-family:"Encode Sans Condensed",sans-serif;font-size:36px;color:var(--orange);padding:12px 0 0 10px}
  .speaker-name{position:absolute;top:546px;left:10px;font-family:"Encode Sans Condensed",sans-serif;font-size:38px;color:var(--ink);white-space:nowrap}
  .schedule{position:absolute;top:614px;left:0;width:400px;height:100px;background:linear-gradient(90deg,var(--navy) 75%,#5f7d9b);font-family:"Open Sans",sans-serif;font-size:20.5px;line-height:31px;color:var(--white);padding:18px 0 0 15px}
  .contact{position:absolute;top:760px;left:0;width:100%;height:116px;background:linear-gradient(90deg,var(--orange) 60%,#f7c98c 100%);font-family:"Open Sans",sans-serif;color:var(--navy);padding:6px 0 0 12px}
  .contact-label{font-family:"Encode Sans Condensed",sans-serif;font-size:27px;color:var(--white);padding-left:7px}
  .contact-line{font-size:22px;line-height:36px;white-space:nowrap}
  .focus{position:absolute;left:364px;top:500px;width:224px;height:376px}
  .focus-word{font-family:"Open Sans",sans-serif;font-size:21px;fill:var(--white)}
  .focus-word.dark{fill:var(--ink)}
</style>
</head>
<body>
<main class="flyer">
  <div class="brand"><span class="brand-dot"></span>SOLVANE</div>
  <h1 class="event-title">LANTERN GATHERING 2018</h1>
  <div class="theme-band" role="img" aria-label="Band of flames"></div>
  <p class="theme">Winds of morning</p>

  <section class="venue">
    <div class="venue-label">The location of the event</div>
    <div>Halvorn Community Center,</div>
    <div>482 Tillman Street, Portland, ME 04107</div>
  </section>

  <div class="speaker-tag">Speaker:</div>
  <div class="speaker-name">Prophet Marcus Obuya</div>

  <section class="schedule">
    <div>December 28th, 29th @ 7:00PM</div>
    <div>December 30th @ 10:00AM</div>
  </section>

  <section class="contact">
    <div class="contact-label">Contact</div>
    <div class="contact-line">contact@cedarbrookhaven.org</div>
    <div class="contact-line">207 555 3184</div>
  </section>

  <svg class="focus" viewBox="0 0 224 376">
    <defs>
      <linearGradient id="fireGrad" x1="0" y1="0" x2="1" y2="1">
        <stop offset="0" stop-color="#2a0d05"/><stop offset=".5" stop-color="#e0621a"/><stop offset="1" stop-color="#f6b63c"/>
      </linearGradient>
      <linearGradient id="revivalGrad" x1="0" y1="0" x2="0" y2="1">
        <stop offset="0" stop-color="#f5e6d4"/><stop offset=".6" stop-color="#e9b58a"/><stop offset="1" stop-color="#7a2a12"/>
      </linearGradient>
      <radialGradient id="propheticGrad" cx=".55" cy=".4" r=".7">
        <stop offset="0" stop-color="#f0b04a"/><stop offset=".5" stop-color="#8a5a2a"/><stop offset="1" stop-color="#2b2418"/>
      </radialGradient>
    </defs>
    <g role="img" aria-label="Fire photograph">
      <path d="M10 22 Q120 -10 224 50 L224 120 L18 110 Q8 60 10 22Z" fill="url(#fireGrad)" stroke="var(--navy)" stroke-width="6"/>
    </g>
    <text class="focus-word" x="50" y="46">FIRE</text>
    <g role="img" aria-label="Worship crowd photograph">
      <path d="M-2 110 Q110 95 224 150 L224 250 L8 242 Q-6 170 -2 110Z" fill="url(#revivalGrad)" stroke="var(--navy)" stroke-width="6"/>
    </g>
    <text class="focus-word dark" x="62" y="144">REVIVAL</text>
    <g role="img" aria-label="Hands holding the globe illustration">
      <path d="M4 240 Q110 230 224 290 L224 380 L40 380 Q2 320 4 240Z" fill="url(#propheticGrad)" stroke="var(--navy)" stroke-width="6"/>
    </g>
    <text class="focus-word" x="50" y="307">PROPHETIC</text>
  </svg>
</main>
</body>
</html>
```